Fancy flyer to entice High School Students

http://quillmarsh.com needs a marketing slick/flyer to pass out. The marketing text is below(feel free to place where you think appropriate).

* 8th grade to 12th grade (or 8th graders to 12th graders)
* Land a real job internship(instead of Grubbins)
* 100's of internships available
* Learn how to start your own business out of High School making way more than minimum wage
* In college when interviewing for an internship don't be the guy that answers "no, sorry, this would be my first internship" putting you at a huge disadvantage"
* Fill in the Contact Us form at http://quillmarsh.com at the bottom left corner to find out more information

We will be evaluating design with this blog post in mind....
http://trovelinkdigest.com/color-influence-buyers/

We like attention grabbing contact us type stuff and calls to action. If you feel it is appropriate to change the marketing text to make your flyer stand out, please feel free. I am not the best at marketing and am the first to admit it.
Updates

A simple 8.5 x 11 flyer would be great.

Target Market(s)

High School students, male and female with high grade point averages(smart students). For the top 20% of their class.

Industry/Entity Type

Marketing

Requirements
Must have
• good call to action

```html
<!DOCTYPE html>
<html lang="en">
<head>
<meta charset="utf-8">
<title>Quillmarsh Software – Real Internships</title>
<link rel="stylesheet" href="https://fonts.googleapis.com/css2?family=Source+Sans+3:wght@400;600;700;800&display=swap">
<style>
  :root {
    --orange: #f7941d;
    --yellow: #fff200;
    --blue: #1a75bb;
    --red: #e3141b;
    --white: #ffffff;
    --ink: #3a3a3a;
  }
  html, body {
    margin: 0;
    padding: 0;
    overflow: hidden;
    background: var(--white);
  }
  .flyer {
    position: relative;
    width: 927px;
    height: 1200px;
    overflow: hidden;
    background: var(--white);
    font-family: "Source Sans 3", "Myriad Pro", Arial, sans-serif;
    color: var(--blue);
  }
  .flyer p, .flyer h1 { white-space: nowrap; }
  .bands {
    position: absolute;
    inset: 0;
  }
  .brand {
    position: absolute;
    left: 16px;
    top: 26px;
    display: flex;
    align-items: center;
    gap: 10px;
    font-size: 29px;
    font-weight: 600;
    color: var(--ink);
  }
  .brand-dot {
    width: 18px;
    height: 18px;
    border-radius: 50%;
    background: var(--ink);
  }
  .lead-in {
    position: absolute;
    left: 338px;
    top: 150px;
    margin: 0;
    font-size: 22px;
    letter-spacing: 0.7px;
  }
  .warn {
    text-decoration: underline;
    text-decoration-color: var(--red);
    text-decoration-thickness: 3px;
    text-underline-offset: 5px;
  }
  .quote-box {
    position: absolute;
    left: 66px;
    top: 195px;
    width: 797px;
    height: 55px;
    margin: 0;
    background: var(--blue);
    color: var(--white);
    font-size: 37px;
    font-weight: 600;
    letter-spacing: 0.6px;
    line-height: 55px;
    text-align: center;
  }
  .follow-up {
    position: absolute;
    left: 66px;
    top: 257px;
    margin: 0;
    font-size: 22px;
    letter-spacing: 0.7px;
  }
  .headline {
    position: absolute;
    left: 0;
    top: 460px;
    margin: 0;
    width: 927px;
    font-weight: 700;
    line-height: 1;
  }
  .headline-top {
    display: block;
    padding-left: 52px;
    font-size: 84px;
    letter-spacing: 1px;
  }
  .headline-main {
    display: block;
    padding-left: 40px;
    margin-top: 6px;
    font-size: 96px;
    font-weight: 800;
    letter-spacing: 6px;
  }
  .count {
    position: absolute;
    left: 42px;
    top: 642px;
    margin: 0;
    font-size: 33px;
    letter-spacing: 0.9px;
  }
  .count strong { font-weight: 700; }
  .pitch {
    position: absolute;
    left: 42px;
    top: 686px;
    margin: 0;
    font-size: 23px;
    letter-spacing: 0.6px;
    line-height: 29px;
    color: var(--orange);
  }
  .grades {
    position: absolute;
    right: 22px;
    top: 846px;
    margin: 0;
    font-size: 54px;
    font-weight: 800;
    line-height: 60px;
    letter-spacing: 2px;
    text-align: right;
    color: var(--white);
  }
  .footer {
    position: absolute;
    left: 0;
    top: 1025px;
    width: 927px;
    height: 175px;
    background: var(--blue);
    color: var(--white);
  }
  .footer .about {
    position: absolute;
    left: 24px;
    top: 24px;
    width: 880px;
    margin: 0;
    font-size: 17.5px;
    letter-spacing: 0.3px;
    line-height: 22px;
    white-space: normal;
  }
  .visit {
    position: absolute;
    left: 0;
    top: 137px;
    width: 927px;
    margin: 0;
    font-size: 19px;
    letter-spacing: 0.5px;
    text-align: center;
  }
</style>
</head>
<body>
<main class="flyer">
  <svg class="bands" width="927" height="1200" viewBox="0 0 927 1200" aria-hidden="true">
    <rect x="0" y="0" width="927" height="980" fill="var(--orange)"/>
    <polygon points="0,0 790,0 0,156" fill="var(--white)"/>
    <polygon points="0,452 927,252 927,272 0,472" fill="var(--white)"/>
    <polygon points="0,480 927,310 927,680 0,858" fill="var(--yellow)"/>
    <polygon points="0,868 927,690 927,706 0,886" fill="var(--white)"/>
  </svg>

  <div class="brand"><span>Quillmarsh Software</span><span class="brand-dot"></span></div>

  <p class="lead-in"><span class="warn">Don’t</span> be the guy at an internship interview that says:</p>
  <p class="quote-box">“No sorry, this would be my first internship”</p>
  <p class="follow-up"><span class="warn">Don’t</span> contemplate working at Fast Food Restaurants either!</p>

  <h1 class="headline">
    <span class="headline-top">LAND YOURSELF IN A</span>
    <span class="headline-main">REAL INTERNSHIP</span>
  </h1>
  <p class="count">We have <strong>HUNDREDS</strong> of internships available for YOU!</p>
  <p class="pitch">Learn how to start your own business and make<br><span class="warn">more</span> than minimum wage!</p>

  <p class="grades">8TH - 12TH GRADERS ARE<br>WELCOMED TO JOIN!</p>

  <footer class="footer">
    <p class="about">Quillmarsh Software is an onshore and offshore company that has consultants in many different disciplines and technologies.&nbsp; We are a team of passionate technologists who love to work on new challenges and are ready to work on any of your technology related needs.</p>
    <p class="visit">Visit us at http://quillmarsh.com for more information</p>
  </footer>
</main>
</body>
</html>
```